Anzeigengestaltung für eine Hausarztpraxis
Zielgruppe
Wir sind eine Hausarztpraxis mit zwei Standorten und suchen eine Ärztin oder einen Arzt zur Anstellung in der klassischen Hausarzt Medizin am Standort Lindwil
Aufgabenstellung
Bitte beachtet den Text im Anhang, der ist schon vorgegeben. (Anzeigentext)
Wir suchen ein ruhiges, hochwertiges Layout für eine Stellenanzeige einer Hausarztpraxis in einem historischen Gebäude.
Der Text steht im Vordergrund, das Design soll zurückhaltend, klar und wertig sein.
Bitte keine Icons, keine bunten Farben, keine verspielten Elemente.
Gerne viel Weissraum, klare Typografie, ruhige Anmutung.
Schrift: Garamond für den Fliesstext (bereits gewählt).
Das Layout soll sowohl als PDF wie auch online funktionieren.
Optional: ein sehr dezentes grafisches Element oder eine ruhige Bildanmutung (z. B. Struktur, Licht, Architekturdetail).

```html
<!DOCTYPE html>
<html lang="de">
<head>
<meta charset="utf-8">
<title>Stellenanzeige Hausarztpraxis Lindwil</title>
<link rel="stylesheet" href="https://fonts.googleapis.com/css2?family=EB+Garamond:ital,wght@0,400;0,600;0,700;1,400&display=swap">
<style>
  :root {
    --page-bg: #f3f3f3;
    --sheet: #ffffff;
    --ink: #2b2b2b;
    --ink-strong: #222222;
    --mark: #2a2f2a;
    --photo-house: linear-gradient(180deg, #d9dcdd 0%, #e9e6df 35%, #8a6a55 55%, #6f7a55 75%, #b9b2a4 100%);
    --photo-room: linear-gradient(90deg, #e2e0dd 0%, #e8e6e2 30%, #f1f0ec 55%, #dedbd3 80%, #cfc7bc 100%);
    --photo-desk: linear-gradient(135deg, #eceae6 0%, #b07a45 40%, #9c6835 60%, #4f6e3a 85%, #cfcac2 100%);
  }
  * { margin: 0; padding: 0; box-sizing: border-box; }
  html, body { width: 1200px; height: 1200px; overflow: hidden; background: var(--page-bg); }
  body { position: relative; font-family: "EB Garamond", Garamond, serif; color: var(--ink); }
  .sheet { position: absolute; left: 32px; top: 32px; width: 1136px; height: 1136px; background: var(--sheet); }
  .abs { position: absolute; }
  .brand { left: 78px; top: 140px; display: flex; align-items: center; gap: 12px; }
  .brand-dot { width: 16px; height: 16px; border-radius: 50%; background: var(--mark); }
  .brand-name { font-size: 22px; font-weight: 600; color: var(--mark); line-height: 1.15; }
  .headline { font-size: 17.5px; font-weight: 700; color: var(--ink-strong); line-height: 20.7px; }
  .body-text { font-size: 17.5px; line-height: 20.7px; }
  .tagline { font-style: italic; font-size: 17.5px; line-height: 20.7px; }
  .contact-mail { left: 80px; top: 972px; font-size: 20px; font-weight: 700; color: var(--ink-strong); }
  .contact-block { left: 80px; top: 1010px; font-size: 20px; line-height: 25.5px; }
  .contact-block strong { font-weight: 700; color: var(--ink-strong); }
</style>
</head>
<body>
  <div class="sheet"></div>

  <div class="abs brand">
    <span class="brand-dot"></span>
    <span class="brand-name">Arztpraxis<br>Lindenhof</span>
  </div>

  <div class="abs photo" role="img" aria-label="Blick in ein helles Behandlungszimmer mit Liege und Schreibtisch" style="left:606px; top:74px; width:519px; height:165px; background:var(--photo-room);"></div>

  <h1 class="abs headline" style="left:73px; top:249px; width:440px;">Hausarztmedizin mit Tiefe – dort, wo man noch echte Grundversorgung lebt</h1>
  <p class="abs tagline" style="left:73px; top:308px;">Ein Ort, der trägt. Ein Team, das bleibt. Eine Arbeit, die Wertschätzung hat.</p>
  <p class="abs body-text" style="left:73px; top:350px; width:530px;">Manche Orte verändern die Art, wie man arbeitet.<br>Unsere Praxis in Lindwil ist so ein Ort.</p>
  <p class="abs body-text" style="left:73px; top:412px; width:528px;">In einem historischen Gebäude gelegen, mit grosszügigem Ambiente, warmen Vertäfelungen und kunstvoller Wandbemalung, entstehen hier Behandlungsräume von Ruhe und Würde. Kein steriler Praxisalltag, sondern ein Ort, der Gespräche trägt und medizinische Arbeit unterstützt.</p>
  <p class="abs body-text" style="left:73px; top:516px; width:525px;">Für diesen besonderen Ort suchen wir eine Hausärztin oder einen Hausarzt, die oder der nicht einfach einen Arbeitsplatz sucht, sondern einen Platz, an dem Medizin menschlich sein darf.</p>

  <div class="abs photo" role="img" aria-label="Historisches Praxisgebäude mit roten Fensterläden und Steingarten mit Brunnen" style="left:74px; top:618px; width:518px; height:329px; background:var(--photo-house);"></div>

  <p class="abs contact-mail">E-Mail: Melina.Korvath@arztpraxis-lindenhof.ch</p>
  <p class="abs contact-block"><strong>Arztpraxis Lindenhof</strong><br>Brunnmattweg 7<br>4735 Lindwil<br>Tel: 0629180417</p>

  <h2 class="abs headline" style="left:620px; top:249px;">Ein Team mit Haltung</h2>
  <p class="abs body-text" style="left:620px; top:291px; width:480px;">Sie arbeiten in einem freundlichen, über Jahre gewachsenen Team mit hoher personeller Kontinuität und geringer Fluktuation.</p>
  <h2 class="abs headline" style="left:620px; top:353px;">Zeit für gute Medizin</h2>
  <p class="abs body-text" style="left:620px; top:395px; width:470px;">Unsere Patientinnen und Patienten sind überwiegend gut bis sehr gut situiert, wertschätzend und therapieoffen. Das ermöglicht ruhiges, strukturiertes Arbeiten mit Fokus auf Qualität, Beziehung und nachhaltige Behandlung.</p>
  <h2 class="abs headline" style="left:620px; top:498px;">Und sonst?</h2>
  <p class="abs body-text" style="left:620px; top:540px; width:500px;">Der Praxisalltag ist klar strukturiert, ruhig und verlässlich. Geregelte und in Abstimmung flexible Arbeitszeiten ohne Wochenend- oder Nachtdienste, eine sehr gute leistungsbezogene Vergütung sowie ein respektvoller, wertschätzender Umgang auf Augenhöhe schaffen ein Umfeld, in dem man sich auf die medizinische Arbeit konzentrieren und langfristig wohlfühlen kann.</p>
  <p class="abs body-text" style="left:620px; top:685px; width:490px;">Wir freuen uns über eine unkomplizierte Kontaktaufnahme per E-Mail oder Telefon – gerne auch ganz unverbindlich und ohne vollständige Bewerbungsunterlagen.</p>

  <div class="abs photo" role="img" aria-label="Empfangsbereich mit antikem Holzschrank, Holztheke und Zimmerpflanzen" style="left:606px; top:779px; width:519px; height:347px; background:var(--photo-desk);"></div>
</body>
</html>
```